Create 8 Featured Images for 8 Blog articles

We're looking for a an individual with a background in graphic design to creatively process images for a popular product blog. This project will be to create 8 Featured images for our Blog which can be seen here http://www.quelvarspas.com/blog the featured image is the large image which can be seen through the link above. If all goes well with this first project then there will be many additional graphic design projects available for our blog.

1. My Pool Pump is Running Too Hot - Article can be seen here http://www.quelvarspas.com/blog/why-is-my-motor-running-hot/ We would like an Image of 750 x 250 of a pool pump in the desert or under the sun. Something obvious. We are trying to convey the message of an extremely hot pump. For the Desert or Sun use an image of your liking and for the pool pump use the attached image labeled “Hot Pump.jpg” (remove text from this image) Add text to image which says "Pool Pump Running Hot?"

2. Leaking pool pump - Article can be seen here http://www.quelvarspas.com/blog/leaking-pool-pump/ Image to be created would be a leaking pool pump which is gushing out water similar to what is shown here http://www.lorvane-tide-care.com/pool-closings.html but we would like for this to look much cleaner. The background of the image should be similar in color and style of the image backgrounds which can be seen here http://www.quelvarspas.com/blog/ For the pool pump use the attached image labeled “Leaking Pump.jpg” and then photoshop gushing water out of the pump. Add text to image which says "Leaking Pool Pump?"

3. Can I go with a higher Horse Power Pump - article can be seen here http://www.quelvarspas.com/blog/can-go-higher-horsepower-pump/ Image of a large pool pump vs. a small pump - You can exagerate the size of the large pump and exagerate the size of the small pump. The idea is to show a really big looking pump vs. a small looking pump. Attached image for the large pump is labeled “Large Pump.jpg” and Attached image of small pump is labeled “Small Pump.jpg” Add text to image which says "Large HP Vs. Small HP"

4. Pool Pump Trips Breaker - Article can be seen here http://www.quelvarspas.com/blog/pool-pump-trips-breaker-gfci/ This will be a simple Image of a pool pump and a breaker spaced out evenly. Use attached image of of pool pump labeled “Pool Pump Breaker.jpg” and for the breaker use the attached image labeled “Breaker.jpg” Add text to image which says "Pool Pump Tripping Breaker?"

5. Why is my spa dirty? - Article can be seen here http://www.quelvarspas.com/blog/spa-dirty/ use attached image labeled spa set on white backgroud with Text which says "Dirty Spa?"

6. Think You’re Cut out to Replace Your Pool Pump Motor? Take This Quiz - Article here -
http://www.quelvarspas.com/blog/think-youre-cut-replace-pool-pump-motor-take-quiz/ Image integrating Quiz.jpg image and motor.jpg image with Text labeled "Take the Pool Motor Replacement Quiz"

7. Can I repair my pool Equipment - article here http://www.quelvarspas.com/blog/can-i-repair-my-pool-equipment/ - A guy holding tools with a question mark thought bubble.

8. How Long should I run my pool pump article here -http://www.quelvarspas.com/blog/how-long-should-i-run-my-pool-pump/ - image of a pool pump along with a man looking at his watch.

```html
<!DOCTYPE html>
<html lang="en">
<head>
<meta charset="utf-8">
<title>Large HP Vs Small HP</title>
<link href="https://fonts.googleapis.com/css2?family=Alice&display=swap" rel="stylesheet">
<style>
  :root {
    --blue-core: #2a5ad8;
    --blue-edge: #0b1f78;
    --gold-core: #ffe04a;
    --gold-edge: #f5a300;
    --badge: #f8c51f;
    --navy: #1c2d63;
    --white: #ffffff;
    --pump-light: #e6dfd0;
    --pump-light-shade: #b9b09e;
    --pump-dark: #2a2a2a;
    --pump-dark-shade: #0d0d0d;
  }
  * { margin: 0; padding: 0; box-sizing: border-box; }
  html, body { width: 1200px; height: 400px; overflow: hidden; background: var(--white); }
  .banner { position: relative; width: 1200px; height: 400px; overflow: hidden; font-family: "Alice", Georgia, serif; }
  .backdrop { position: absolute; inset: 0; }
  .pump { position: absolute; }
  .pump--large {
    left: 30px; top: 92px; width: 500px; height: 300px;
    border-radius: 44px 70px 34px 34px;
    background: linear-gradient(160deg, var(--pump-light) 0%, var(--pump-light-shade) 100%);
  }
  .pump--small {
    left: 850px; top: 90px; width: 230px; height: 140px;
    border-radius: 24px 30px 16px 16px;
    background: linear-gradient(160deg, var(--pump-dark) 0%, var(--pump-dark-shade) 100%);
  }
  .label {
    position: absolute;
    font-size: 52px;
    line-height: 1;
    white-space: nowrap;
  }
  .label--large { left: 160px; top: 24px; color: var(--white); }
  .label--small { left: 808px; top: 316px; color: var(--navy); }
  .versus {
    position: absolute; left: 541px; top: 144px;
    width: 112px; height: 112px; border-radius: 50%;
    background: var(--badge);
    display: flex; align-items: center; justify-content: center;
    color: var(--navy); font-size: 46px;
  }
  .arrows { position: absolute; inset: 0; }
</style>
</head>
<body>
<div class="banner">
  <svg class="backdrop" width="1200" height="400" viewBox="0 0 1200 400">
    <defs>
      <radialGradient id="blueGlow" cx="597" cy="200" r="640" gradientUnits="userSpaceOnUse">
        <stop offset="0" stop-color="var(--blue-core)"/>
        <stop offset="1" stop-color="var(--blue-edge)"/>
      </radialGradient>
      <radialGradient id="goldGlow" cx="620" cy="200" r="620" gradientUnits="userSpaceOnUse">
        <stop offset="0" stop-color="var(--gold-core)"/>
        <stop offset="1" stop-color="var(--gold-edge)"/>
      </radialGradient>
    </defs>
    <rect class="side-gold" width="1200" height="400" fill="url(#goldGlow)"/>
    <g class="rays-gold" fill="#ffffff" opacity="0.16">
      <polygon points="597,200 1200,0 1200,70"/>
      <polygon points="597,200 1200,150 1200,230"/>
      <polygon points="597,200 1200,330 1200,400"/>
      <polygon points="597,200 900,0 1000,0"/>
      <polygon points="597,200 760,400 860,400"/>
    </g>
    <polygon class="side-blue" points="0,0 664,0 544,400 0,400" fill="url(#blueGlow)"/>
    <g class="rays-blue" fill="#ffffff" opacity="0.08">
      <polygon points="597,200 0,0 0,80"/>
      <polygon points="597,200 0,160 0,240"/>
      <polygon points="597,200 0,330 0,400"/>
      <polygon points="597,200 220,0 330,0"/>
      <polygon points="597,200 200,400 300,400"/>
    </g>
  </svg>

  <div class="pump pump--large" role="img" aria-label="Large beige pool pump with clear strainer lid, shown oversized"></div>
  <div class="pump pump--small" role="img" aria-label="Small black pool pump with strainer basket and motor, shown undersized"></div>

  <svg class="arrows" width="1200" height="400" viewBox="0 0 1200 400" fill="none">
    <g stroke="var(--gold-core)" stroke-width="3" stroke-linecap="round">
      <path d="M590 140 C 575 85, 500 45, 412 38"/>
      <path d="M426 26 L 410 38 L 426 50"/>
    </g>
    <g stroke="var(--navy)" stroke-width="3" stroke-linecap="round">
      <path d="M590 262 C 605 320, 690 346, 792 348"/>
      <path d="M778 336 L 794 348 L 778 360"/>
    </g>
  </svg>

  <div class="label label--large">Large HP</div>
  <div class="versus">Vs</div>
  <div class="label label--small">Small HP</div>
</div>
</body>
</html>
```